Flyer Design Project

I am starting a new Cake Business called "FROSTED HOUR" and want flyers. The main product are Cupcakes and will be marketed for parties/events/celebrations to order. Other cakes can be made to order (Christmas/Birthday etc)

Industry/Entity Type

Business

Requirements
Must have
• Contact Telephone Number

```html
<!DOCTYPE html>
<html lang="en">
<head>
<meta charset="utf-8">
<title>Frosted Hour – Cupcake Flyer</title>
<link rel="stylesheet" href="https://fonts.googleapis.com/css2?family=Dancing+Script:wght@500&family=Caveat:wght@500&display=swap">
<style>
  :root {
    --pink-light: #f7c6ea;
    --pink-mid: #ef8fd6;
    --pink-deep: #e46cc3;
    --wine: #8c1824;
    --strip: #8e1414;
    --ink: #5a0f1c;
    --text-dark: #2a0f14;
  }
  * { margin: 0; padding: 0; box-sizing: border-box; }
  html, body { width: 849px; height: 1200px; overflow: hidden; background: #ffffff; }
  .flyer { position: relative; width: 849px; height: 1200px; overflow: hidden; }

  .backdrop-photo {
    position: absolute; inset: 0;
    background:
      radial-gradient(ellipse 260px 220px at 700px 930px, #f08ad3 0%, rgba(240,138,211,0) 100%),
      radial-gradient(ellipse 200px 200px at 460px 820px, #ee9ad8 0%, rgba(238,154,216,0) 100%),
      radial-gradient(circle 50px at 420px 600px, #e65aa8 0%, rgba(230,90,168,0) 100%),
      radial-gradient(circle 50px at 760px 680px, #e2509f 0%, rgba(226,80,159,0) 100%),
      linear-gradient(160deg, var(--pink-light) 0%, var(--pink-mid) 55%, var(--pink-deep) 100%);
  }

  .photo-strip {
    position: absolute; left: 67px; top: 0; width: 256px; height: 1200px;
    background: var(--strip);
  }
  .strip-photo { position: absolute; left: 17px; width: 222px; }
  .strip-photo.berry { top: 18px; height: 336px;
    background: radial-gradient(ellipse at 55% 60%, #5a0b22 0%, #7a1a33 45%, #e9e4df 80%); }
  .strip-photo.mocha { top: 368px; height: 297px;
    background: radial-gradient(ellipse at 45% 55%, #c48d5c 0%, #8a5a3a 45%, #2b1a14 100%); }
  .strip-photo.chocolate { top: 681px; height: 330px;
    background: radial-gradient(ellipse at 50% 50%, #4a2416 0%, #6b3420 50%, #c46ad6 100%); }
  .strip-photo.tiered { top: 1029px; height: 149px;
    background: linear-gradient(180deg, #6b4a3a 0%, #3a1f16 45%, #e4581e 60%, #3a1f16 100%); }

  .brand-title {
    position: absolute; left: 370px; top: 98px; width: 440px; text-align: center;
    font-family: "Dancing Script", cursive; font-weight: 500;
    font-size: 66px; color: var(--wine); line-height: 1;
  }

  .offer {
    position: absolute; font-family: "Dancing Script", cursive; font-weight: 500;
    color: var(--wine); font-size: 38px; line-height: 54px;
  }
  .offer.main { left: 385px; top: 345px; }
  .offer.special { left: 372px; top: 655px; }

  .contact {
    position: absolute; left: 370px; top: 1058px;
    font-family: "Caveat", cursive; font-weight: 500;
    font-size: 25px; color: var(--text-dark);
  }
  .contact .number { margin-left: 26px; font-family: Arial, sans-serif; font-size: 14px; letter-spacing: 1px; vertical-align: middle; }
</style>
</head>
<body>
  <main class="flyer">
    <div class="backdrop-photo" role="img" aria-label="Close-up photo of pink frosted cupcakes topped with cherries"></div>

    <aside class="photo-strip">
      <div class="strip-photo berry" role="img" aria-label="Photo of a cheesecake cup topped with berry compote"></div>
      <div class="strip-photo mocha" role="img" aria-label="Photo of chocolate cupcakes with mocha frosting"></div>
      <div class="strip-photo chocolate" role="img" aria-label="Photo of chocolate frosted cupcakes on a plate"></div>
      <div class="strip-photo tiered" role="img" aria-label="Photo of a tiered chocolate cake decorated with orange flowers"></div>
    </aside>

    <h1 class="brand-title">"Frosted Hour"</h1>

    <p class="offer main">Order cup cakes now for,<br>parties<br>events &amp; celebrations<br>you name it!!</p>
    <p class="offer special">Special orders&nbsp; for,<br>Birthdays / Christmas etc.</p>

    <p class="contact">call us now on ~:<span class="number">*****************</span></p>
  </main>
</body>
</html>
```